I need a new business card design for my pharmacy.

I need a business card design. I will include my logo.
The card needs to be readable. I prefer to have my logo on one side along with my website, the other side includes the other information. Please use combination of black, neon green, white, and silver. This needs to catch the eye but yet be clearly visible and legible. Thanks

Industry/Entity Type

Pharmacy

Contact Information for Business Card

It needs to have the following information listed:
Vel's Apothecary Owner/Pharm D.
7143 North Birch Lane
Sioux Falls, SD 57362
Phone 605-318-6027
Fax 605-318-6025
email: vel@velsapothecary.example
www.velsapothecary.example
Store hours Monday-Friday 8 am- 7 pm
Saturday 8 am- 12 pm
Sunday Closed
Please utilize the colors black, white, and neon green, maybe silver.

Requirements
Must have
• It needs to be easily readable!
Nice to have
• It should catch the eye.
Should not have
• Do not use any other colors except listed: black, neon green, white, & silver.

```html
<!DOCTYPE html>
<html lang="en">
<head>
<meta charset="utf-8">
<title>Vel's Apothecary — Business Card</title>
<link rel="stylesheet" href="https://fonts.googleapis.com/css2?family=Arimo:wght@400;700&family=Open+Sans:wght@600&family=Oswald:wght@300;400&display=swap">
<style>
  :root {
    --backdrop: #1dae9a;
    --card: #ffffff;
    --ink: #1f1f1f;
    --neon: #39f01a;
    --label-green: #5cd43a;
    --silver: #b8b8b8;
    --silver-text: #a9a9a9;
  }
  * { margin: 0; padding: 0; box-sizing: border-box; }
  html, body { width: 1200px; height: 1000px; overflow: hidden; }
  body {
    background: var(--backdrop);
    position: relative;
    font-family: "Arimo", Arial, sans-serif;
    color: var(--ink);
  }
  .card {
    position: absolute;
    top: 310px;
    width: 560px;
    height: 360px;
    background: var(--card);
  }
  .card--info { left: 10px; }
  .card--brand { left: 631px; }

  .title-block { position: absolute; left: 94px; top: 38px; }
  .title-block .role { font-size: 14px; letter-spacing: 0.2px; text-transform: uppercase; }
  .title-block .company { font-size: 15px; font-weight: 700; text-transform: uppercase; margin-top: 2px; }

  .brand-square {
    position: absolute; left: 95px; top: 90px;
    width: 145px; height: 153px;
    background: var(--ink);
    display: flex; align-items: flex-end; justify-content: center;
    padding-bottom: 16px;
  }
  .brand-square .brand-name {
    font-family: "Open Sans", Arial, sans-serif;
    font-weight: 600; font-size: 19px; color: #fff; letter-spacing: -0.6px;
  }

  .contact-rule {
    position: absolute; left: 280px; top: 92px;
    width: 1px; height: 150px; background: var(--ink);
  }
  .contact-list { position: absolute; left: 291px; top: 90px; list-style: none; }
  .contact-list li { margin-bottom: 4px; font-size: 13px; line-height: 15px; }
  .contact-list .label { display: block; color: var(--label-green); font-size: 13px; }

  .hours-tag {
    position: absolute; left: 235px; width: 91px; height: 16px;
    background: var(--neon);
    font-family: "Oswald", Arial, sans-serif; font-weight: 300;
    font-size: 11px; line-height: 16px; text-align: center; color: var(--ink);
    text-transform: uppercase;
  }
  .hours-tag--top { top: 276px; }
  .hours-tag--bottom { top: 325px; }
  .hours-divider {
    position: absolute; left: 280px; top: 292px; width: 1px; height: 33px; background: var(--silver);
  }
  .hours-line {
    position: absolute; top: 303px;
    font-family: "Oswald", Arial, sans-serif; font-weight: 300;
    font-size: 12px; letter-spacing: 4.2px; text-transform: uppercase; white-space: nowrap;
  }
  .hours-line--weekday { right: 283px; }
  .hours-line--weekend { left: 289px; }

  .brand-lockup {
    position: absolute; left: 0; right: 0; top: 180px;
    display: flex; align-items: center; justify-content: center; gap: 14px;
  }
  .brand-lockup .dot { width: 16px; height: 16px; border-radius: 50%; background: var(--neon); }
  .brand-lockup .brand-name {
    font-family: "Open Sans", Arial, sans-serif; font-weight: 600;
    font-size: 46px; letter-spacing: -1.5px; color: var(--ink);
  }
  .web-row {
    position: absolute; left: 0; right: 0; top: 311px;
    display: flex; align-items: center;
  }
  .web-row .rule { flex: 1; height: 1px; background: var(--silver); }
  .web-row .url { padding: 0 2px; font-size: 16px; color: var(--silver-text); }
</style>
</head>
<body>
  <section class="card card--info" aria-label="Contact side">
    <div class="title-block">
      <p class="role">Owner/Pharm.D</p>
      <p class="company">Vel's Apothecary</p>
    </div>
    <div class="brand-square"><span class="brand-name">Vel's Apothecary</span></div>
    <div class="contact-rule"></div>
    <ul class="contact-list">
      <li><span class="label">Phone</span>605-318-6027</li>
      <li><span class="label">Fax</span>605-318-6025</li>
      <li><span class="label">E-mail</span>vel@velsapothecary.example</li>
      <li><span class="label">Address</span>7143 North Birch Lane Sioux Falls,<br>SD 57362</li>
    </ul>
    <div class="hours-tag hours-tag--top">Store Hours</div>
    <div class="hours-divider"></div>
    <p class="hours-line hours-line--weekday">Monday-Friday 8am-7pm.</p>
    <p class="hours-line hours-line--weekend">Saturday 8am-12pm.</p>
    <div class="hours-tag hours-tag--bottom">Sunday Closed</div>
  </section>

  <section class="card card--brand" aria-label="Brand side">
    <div class="brand-lockup">
      <span class="dot"></span>
      <span class="brand-name">Vel's Apothecary</span>
    </div>
    <div class="web-row">
      <span class="rule"></span>
      <span class="url">www.velsapothecary.example</span>
      <span class="rule"></span>
    </div>
  </section>
</body>
</html>
```